Tarvil GmbH business card

We Tarvil GmbH based in Switzerland are looking for a business card design. The Fresh Jung, appealing to customers of all kinds. We already have a logo to upload but still a business card. Details: Tarvil GmbH Address: Lindenweg 14b in 9412 Rudolfen. Tel: 41 76 392 00 47, web: Tarvil.ch, E-mail: info@Tarvil.ch Facebook: Tarvil GmbH. I am the Managing Director: Lukas Verholt. On reverse: Title: Transporter and bus rental Gross: Without deposit Super prices
Contact Information for Business Card
Siehe Projektbeschreibung
Requirements
Should not have
- Other pictures

```html
<!DOCTYPE html>
<html lang="en">
<head>
<meta charset="utf-8">
<title>Tarvil GmbH – Business Card</title>
<link rel="stylesheet" href="https://fonts.googleapis.com/css2?family=Source+Sans+3:wght@400;600&display=swap">
<style>
  :root {
    --backdrop: #3b3430;
    --card: #0c0c0c;
    --card-edge: #1a1a1a;
    --brand-blue: #1c1a8e;
    --name-blue: #8ea3c4;
    --text-light: #e6e6e6;
    --divider: #2c2c2c;
    --silver: #c9c9c9;
    --silver-soft: #8a8a8a;
  }
  * { margin: 0; padding: 0; box-sizing: border-box; }
  html, body {
    width: 1200px;
    height: 900px;
    overflow: hidden;
    background: var(--backdrop);
    font-family: "Source Sans 3", "Myriad Pro", Arial, sans-serif;
  }
  .stage {
    position: relative;
    width: 1200px;
    height: 900px;
    display: flex;
    align-items: center;
    justify-content: center;
    gap: 50px;
  }
  .card {
    position: relative;
    width: 520px;
    height: 300px;
    background: var(--card);
    border: 1px solid var(--card-edge);
    border-radius: 3px;
    box-shadow: 0 10px 24px rgba(0, 0, 0, 0.45);
  }

  /* Contact side */
  .card--contact { display: flex; align-items: center; }
  .brand-mark {
    width: 250px;
    display: flex;
    align-items: center;
    justify-content: center;
    font-size: 58px;
    font-weight: 600;
    color: var(--brand-blue);
    letter-spacing: 1px;
  }
  .divider {
    width: 1px;
    height: 190px;
    background: var(--divider);
  }
  .details {
    padding-left: 30px;
    color: var(--text-light);
    font-size: 15px;
    line-height: 1.3;
  }
  .details .person { font-size: 18px; font-weight: 600; color: var(--name-blue); }
  .details .role { margin-bottom: 18px; }
  .details .address { margin-bottom: 16px; }
  .contact-list { list-style: none; }
  .contact-list li { display: flex; align-items: center; gap: 10px; }
  .contact-list svg { width: 11px; height: 11px; fill: var(--name-blue); flex: none; }

  /* Brand side */
  .card--brand {
    display: flex;
    align-items: center;
    justify-content: center;
  }
  .brand-name {
    font-size: 46px;
    font-weight: 600;
    color: var(--silver);
    letter-spacing: 2px;
  }
</style>
</head>
<body>
<main class="stage">
  <section class="card card--contact">
    <div class="brand-mark">Tarvil</div>
    <div class="divider"></div>
    <div class="details">
      <p class="person">Jonathan Smith</p>
      <p class="role">Managing Director</p>
      <p class="address">12345, Address Goes Here<br>Country Name, 123456.</p>
      <ul class="contact-list">
        <li>
          <svg viewBox="0 0 12 12" aria-hidden="true"><path d="M2.4 1l2 2.2-1 1.3c.8 1.6 2 2.8 3.6 3.6l1.3-1 2.2 2-1 1.8C5.3 10.7 1.3 6.7 1 1.9z"/></svg>
          044-123 456 789
        </li>
        <li>
          <svg viewBox="0 0 12 12" aria-hidden="true"><path d="M1 2.5h10v7H1z M1.6 3l4.4 3.4L10.4 3z" fill-rule="evenodd"/></svg>
          info@webname.com
        </li>
        <li>
          <svg viewBox="0 0 12 12" aria-hidden="true"><circle cx="6" cy="6" r="5"/></svg>
          www.websitename.com
        </li>
      </ul>
    </div>
  </section>

  <section class="card card--brand">
    <p class="brand-name">Tarvil GmbH</p>
  </section>
</main>
</body>
</html>
```